Radiant Crossing - An Exciting Mission & Book Cover Project

Help me to inspire people to live their best life! This is a mission, not just a design project.
I need a Book Cover designed to keep me inspired on the process of writing my book.
Book Title: Radiant Crossing
Tag Line: Three Simple Steps to get out of your own way, SuperCharge your Life and Step into Purpose!
Author: Marlis Quenby

The three steps are: Ownership, Vision and Action (Not sure if this should be on the front or back of the book cover)

The book is a self-help, motivational book. Personal development.
The cover needs to be strong and capture peoples attention, especially with competing shelf space. I almost see a fire ball of flame or explosion that will grab peoples attention.
My company is The Lantern Institute. I have added the company logo and a few pages of my presentation and topic outline to give an idea.
Maybe: The Lantern Institute logo on back of the cover. website is marlisquenby.com

THOUGHT: People should be able to take a photo of them holding the book cover showing what area of life they want Radiant Crossing in. This is why the front cover must be so visual and powerful that they want to take a photo with it. Ie. Explosion, fire, strong and bold.

Target Market(s)

Anyone who feels stuck and needs to breakthrough and move forward in life.

Industry/Entity Type

Motivation

Font styles to use
Serif
Sans Serif

Colors
ec1f27
f37122
fbed22

Requirements
Must have
• The design must be STRONG, SIMPLE, STAND OUT ON BOOK SHELVES.
Must have an open file to swap the photo and copy out.

Back Cover Page
1) Summary
2) 2-3 testimonials. One sentence.
3) About the Author (maybe with photo)
4) Lantern Institute logo
5) Website: radiantcrossing.com and marlisquenby.com
Nice to have
• If my photo works somewhere that would be great. I will change the photo later.
Added Where's Your Harbor? a nice cover example.
Should not have
• Right now I am writing the summary for the back of the cover. For now use Loreum Ipsum text and 2-3 recommendations. Again, I will get these only later.

```html
<!DOCTYPE html>
<html lang="en">
<head>
<meta charset="utf-8">
<title>Radiant Crossing – Book Cover Wrap</title>
<link rel="stylesheet" href="https://fonts.googleapis.com/css2?family=Tinos:wght@400;700&family=Cinzel:wght@400;700&family=Jost:wght@400;500;700&display=swap">
<style>
  :root {
    --bg: #dddddd;
    --ink: #111111;
    --paper: #ffffff;
    --green: #6fd12a;
    --lime: #c8e82a;
    --yellow: #fbed22;
    --orange: #f37122;
    --red: #ec1f27;
    --crimson: #d4102a;
    --magenta: #e0237a;
    --violet: #8a1fd0;
    --indigo: #4a1bc4;
  }
  * { box-sizing: border-box; margin: 0; padding: 0; }
  html, body { width: 1200px; height: 800px; overflow: hidden; background: var(--bg); }

  .cover-wrap {
    position: absolute;
    left: 105px; top: 55px;
    width: 990px; height: 690px;
    display: grid;
    grid-template-columns: 460px 70px 460px;
    box-shadow: 0 10px 30px rgba(0,0,0,.18);
  }
  .burst-art {
    position: absolute; inset: 0;
    background:
      radial-gradient(ellipse 38% 45% at 68% 52%, rgba(210,10,30,.95) 0%, rgba(236,31,39,.7) 45%, rgba(236,31,39,0) 100%),
      radial-gradient(ellipse 30% 50% at 92% 50%, rgba(74,27,196,.95) 0%, rgba(138,31,208,.6) 55%, rgba(138,31,208,0) 100%),
      linear-gradient(90deg, var(--green) 0%, var(--lime) 12%, var(--yellow) 26%, var(--orange) 40%, var(--red) 52%, var(--crimson) 66%, var(--magenta) 80%, var(--violet) 92%, var(--indigo) 100%);
  }

  .back-cover, .spine, .front-cover { position: relative; height: 100%; }

  /* back cover */
  .back-cover {
    display: flex; flex-direction: column;
    padding: 92px 40px 34px 70px;
    font-family: "Tinos", "Times New Roman", serif; color: var(--ink);
  }
  .summary p { font-size: 11.5px; line-height: 1.3; margin-bottom: 12px; width: 360px; }
  .testimonials-heading { font-size: 19px; font-weight: 400; margin: 14px 0 6px; }
  .testimonial { font-size: 11.5px; line-height: 1.3; margin-bottom: 9px; padding-left: 12px; width: 380px; }
  .author-block {
    display: grid;
    grid-template-columns: 64px 1fr;
    column-gap: 14px;
    margin-top: 12px;
  }
  .author-photo { grid-row: 1 / span 2; width: 64px; height: 64px; background: var(--paper); }
  .author-heading { font-size: 19px; font-weight: 400; padding-top: 8px; }
  .author-bio { font-size: 11.5px; line-height: 1.3; width: 330px; margin-top: 6px; }
  .back-footer {
    margin-top: auto;
    display: flex; justify-content: space-between; align-items: flex-end;
    padding-right: 0;
  }
  .publisher { display: flex; align-items: center; gap: 8px; font-family: "Jost", sans-serif; font-weight: 500; font-size: 15px; text-transform: uppercase; }
  .publisher-dot { width: 18px; height: 18px; border-radius: 50%; background: var(--orange); }
  .website { font-family: "Jost", sans-serif; font-size: 17px; }

  /* spine */
  .spine { display: flex; flex-direction: column; align-items: center; justify-content: space-between; padding: 24px 0 30px; }
  .spine-title, .spine-author { writing-mode: vertical-rl; }
  .spine-title { font-family: "Tinos", serif; font-weight: 700; color: var(--paper); font-size: 36px; }
  .spine-title small { font-size: 19px; margin-top: 8px; }
  .spine-author { font-family: "Jost", sans-serif; font-size: 21px; color: var(--ink); text-transform: uppercase; }

  /* front cover */
  .front-cover { color: var(--paper); text-align: center; }
  .book-title { position: absolute; top: 150px; left: 0; right: 0; font-family: "Tinos", serif; font-weight: 700; line-height: .9; }
  .book-title .title-main { display: block; font-size: 84px; }
  .book-title .title-sub { display: block; font-size: 38px; text-align: right; padding-right: 46px; }
  .tagline {
    position: absolute; top: 305px; left: 40px; right: 40px;
    font-family: "Cinzel", serif; font-size: 18px; line-height: 1.3; letter-spacing: .5px;
  }
  .tagline b { font-weight: 700; }
  .front-author {
    position: absolute; right: 30px; bottom: 66px;
    font-family: "Jost", sans-serif; font-size: 38px; color: var(--ink); text-transform: uppercase;
  }
  .name-first { font-weight: 700; }
  .name-last { font-weight: 400; }
</style>
</head>
<body>
  <main class="cover-wrap">
    <div class="burst-art" role="img" aria-label="Colour explosion artwork radiating from the front cover, green and yellow on the back through orange and red to magenta and violet"></div>

    <section class="back-cover">
      <div class="summary">
        <p>THOUGHT: People should be able to take a photo of them holding the book cover showing what area of life they want radiant crossing in. This is why the front cover must be so visual and powerful that they want to take a photo with it. Ie. Explosion, fire, strong and bold.</p>
        <p>THOUGHT: People should be able to take a photo of them holding the book cover showing what area of life they want radiant crossing in. This is why the front cover must be so visual and powerful that they want to take a photo with it. Ie. Explosion, fire, strong and bold.</p>
        <p>THOUGHT: People should be able to take a photo of them holding the book cover showing what area of life they want radiant crossing in. This is why the front cover must be so visual and powerful that they want to take a photo with it. Ie. Explosion, fire, strong and bold.</p>
      </div>
      <h2 class="testimonials-heading">testimonials</h2>
      <p class="testimonial">Help me to inspire people to live their best life! This is a mission, not just a design project.</p>
      <p class="testimonial">I need a Book Cover designed to keep me inspired on the process of writing my book.</p>
      <p class="testimonial">I need a Book Cover designed to keep me inspired on the process of writing my book.</p>
      <div class="author-block">
        <div class="author-photo" role="img" aria-label="Author photo placeholder"></div>
        <h2 class="author-heading">About the Author</h2>
        <p class="author-bio">THOUGHT: People should be able to take a photo of them holding the book cover showing what area of life they want radiant crossing in. This is why the front cover must be so visual and powerful that they want to take a photo with it. Ie. Explosion, fire, strong and bold.</p>
      </div>
      <footer class="back-footer">
        <div class="publisher"><span class="publisher-dot"></span>The Lantern Institute</div>
        <div class="website">marlisquenby.com</div>
      </footer>
    </section>

    <section class="spine">
      <div class="spine-title">Radiant <small>Crossing</small></div>
      <div class="spine-author"><span class="name-first">Marlis</span><span class="name-last">Quenby</span></div>
    </section>

    <section class="front-cover">
      <h1 class="book-title">
        <span class="title-main">Radiant</span>
        <span class="title-sub">Crossing</span>
      </h1>
      <p class="tagline">
        <b>Three Simple Steps</b> to<br>
        get out of your <b>own way</b><br>
        <b>Supercharge</b> your life and<br>
        <b>step</b> into <b>purpose!</b>
      </p>
      <div class="front-author"><span class="name-first">Marlis</span><span class="name-last">Quenby</span></div>
    </section>
  </main>
</body>
</html>
```